Solar energy proposal for homeowners

I am providing households with solar energy proposals, and I need a high-quality brochure that is packaged cleverly to attract the homeowner's attention. Take a look at the one page solar brochure that I have included to get an idea of text and content.

Target Market(s)

Residential Homeowners

Industry/Entity Type

Solar

Requirements
Must have
• High quality document

```html
<!DOCTYPE html>
<html lang="en">
<head>
<meta charset="utf-8">
<title>Brightvale Energy – Solar Flyer</title>
<link href="https://fonts.googleapis.com/css2?family=Barlow:wght@400;500;600;700&family=Barlow+Semi+Condensed:wght@400;500;600;700&display=swap" rel="stylesheet">
<style>
:root{
  --navy:#25286a;
  --navy-deep:#1e2160;
  --teal:#1fa9d6;
  --band:#1fb1b3;
  --lime:#b5e21c;
  --ink:#3a3d4a;
  --white:#ffffff;
  --page:#d7d8da;
}
*{margin:0;padding:0;box-sizing:border-box}
html,body{width:1200px;height:2307px;overflow:hidden;background:var(--page)}
body{position:relative;font-family:"Barlow",Arial,sans-serif}
.flyer{
  position:absolute;left:50px;top:375px;width:828px;height:1171px;
  transform:scale(1.3285);transform-origin:0 0;
  background:var(--white);overflow:hidden;
  box-shadow:0 10px 30px rgba(0,0,0,.25);
}
.hero{position:absolute;left:0;top:0;width:828px;height:490px;background:linear-gradient(160deg,#2a2e74,var(--navy-deep))}
.hero-photo{position:absolute;left:0;top:0}
.brand{position:absolute;left:57px;top:74px;display:flex;align-items:center;gap:12px}
.brand-dot{width:36px;height:36px;border-radius:50%;background:var(--teal)}
.brand-name{font-family:"Barlow",sans-serif;font-weight:500;font-size:38px;color:var(--teal);letter-spacing:.3px}
.headline{position:absolute;left:57px;top:178px;color:var(--white);font-family:"Barlow Semi Condensed",sans-serif}
.headline .lead{display:block;font-size:40px;font-weight:400;line-height:38px}
.headline .offer{display:block;font-size:84px;font-weight:700;line-height:72px;margin-top:4px;
  background:linear-gradient(90deg,var(--teal) 0%,#4cc0b0 45%,var(--lime) 75%);
  -webkit-background-clip:text;background-clip:text;color:transparent}
.headline .punch{display:block;font-size:68px;font-weight:400;line-height:60px}
.tagline{position:absolute;left:57px;top:422px;width:402px;height:36px;padding:0 0 0 9px;
  display:flex;align-items:center;
  border-top:1px solid rgba(255,255,255,.7);border-bottom:1px solid rgba(255,255,255,.4);
  color:var(--white);font-family:"Barlow Semi Condensed",sans-serif;font-weight:600;font-size:22px;white-space:nowrap}
.about{position:absolute;left:58px;top:527px;width:390px;color:var(--ink)}
.section-title{font-family:"Barlow Semi Condensed",sans-serif;font-weight:700;font-size:25px;color:var(--teal);text-transform:uppercase}
.about p{font-size:14.5px;line-height:19px;margin-top:4px}
.why{margin-top:14px}
.why-list{display:grid;grid-template-columns:155px 1fr;font-size:15px;font-weight:500;line-height:19px;list-style:none;margin-top:6px}
.why-list li::before{content:"• "}
.panel-photo{position:absolute;left:0;top:785px;width:355px;height:295px;
  background:linear-gradient(135deg,#2d48b8,#4f6fd8 50%,#cfd6ea)}
.services{position:absolute;left:464px;top:490px;width:364px;height:590px;
  background:linear-gradient(180deg,#2f5a62 0%,#27366e 22%,var(--navy) 55%,var(--navy-deep) 100%);
  padding:37px 0 0 32px}
.services .section-title{color:var(--lime);font-size:27px}
.service{display:flex;gap:14px;margin-top:22px;padding-bottom:16px;border-bottom:1px solid rgba(255,255,255,.12);width:290px}
.service:last-child{border-bottom:none}
.service svg{flex:0 0 auto}
.service h3{font-weight:500;font-size:15.5px;color:var(--teal)}
.service p{font-size:14.5px;font-weight:500;line-height:18px;color:var(--white)}
.contact-band{position:absolute;left:0;top:1081px;width:828px;height:90px;background:var(--band);color:var(--white)}
.address{position:absolute;left:48px;top:13px;display:flex;gap:8px;font-size:15.5px;font-weight:500;line-height:20px}
.phone{position:absolute;left:269px;top:0;width:300px;height:90px;background:var(--lime);border-radius:50px/45px;
  display:flex;align-items:center;justify-content:center;gap:8px;
  font-family:"Barlow Semi Condensed",sans-serif;font-weight:700;font-size:38px;color:var(--navy)}
.web{position:absolute;left:584px;top:24px;font-size:15.5px;font-weight:500;line-height:20px}
.web div{display:flex;align-items:center;gap:6px}
</style>
</head>
<body>
<main class="flyer">
  <section class="hero">
    <svg class="hero-photo" width="828" height="490" role="img" aria-label="Photo of a modern house with rooftop solar panels at dusk">
      <defs>
        <linearGradient id="sky" x1="0" y1="0" x2="0" y2="1">
          <stop offset="0" stop-color="#4a5d9e"/>
          <stop offset=".45" stop-color="#8b93b8"/>
          <stop offset=".6" stop-color="#c9a98a"/>
          <stop offset=".72" stop-color="#4e8a34"/>
          <stop offset="1" stop-color="#3b6d27"/>
        </linearGradient>
      </defs>
      <path d="M469 0 C395 140 395 380 520 490 L828 490 L828 0 Z" fill="url(#sky)"/>
    </svg>
    <div class="brand"><span class="brand-dot"></span><span class="brand-name">Brightvale Energy</span></div>
    <h1 class="headline">
      <span class="lead">SOLAR FOR</span>
      <span class="offer">$0 DOWN.</span>
      <span class="punch">NO LIENS.</span>
      <span class="punch">NO KIDDING.</span>
    </h1>
    <div class="tagline">Power Your Future with Brightvale Energy</div>
  </section>

  <section class="about">
    <h2 class="section-title">About Us</h2>
    <p>At Brightvale Energy, our mission is to make solar simple and accessible for everyone. No high-pressure sales—just the information you need to make a smart choice. With our solar rental program, you can lower your monthly energy costs and pay less than your current electricity bill.</p>
    <div class="why">
      <h2 class="section-title">Why Choose Us?</h2>
      <ul class="why-list">
        <li>No financing</li><li>No insurance costs</li>
        <li>No liens</li><li>No long-term commitment</li>
        <li>No down payment</li><li>No maintenance costs</li>
      </ul>
    </div>
  </section>

  <div class="panel-photo" role="img" aria-label="Photo of a row of blue solar panels"></div>

  <section class="services">
    <h2 class="section-title">Our Best Service</h2>
    <div class="service">
      <svg width="66" height="66" viewBox="0 0 66 66"><path d="M33 3a30 30 0 0 1 0 60" fill="none" stroke="#b5e21c" stroke-width="3"/><path d="M33 63a30 30 0 0 1 0-60" fill="none" stroke="#1fa9d6" stroke-width="3"/><circle cx="33" cy="30" r="9" fill="none" stroke="#fff" stroke-width="2"/><rect x="29" y="39" width="8" height="7" fill="none" stroke="#fff" stroke-width="2"/></svg>
      <div><h3>Affordable &amp; Transparent</h3><p>Simple pricing, no hidden fees and a fixed monthly rate lower than typical energy bills.</p></div>
    </div>
    <div class="service">
      <svg width="66" height="66" viewBox="0 0 66 66"><path d="M33 3a30 30 0 0 1 0 60" fill="none" stroke="#1fa9d6" stroke-width="3"/><path d="M33 63a30 30 0 0 1 0-60" fill="none" stroke="#b5e21c" stroke-width="3"/><circle cx="33" cy="33" r="12" fill="none" stroke="#fff" stroke-width="2" stroke-dasharray="4 3"/><circle cx="33" cy="33" r="5" fill="none" stroke="#fff" stroke-width="2"/></svg>
      <div><h3>Expert Installation</h3><p>Certified professionals handle installation, maintenance, and repairs end to end.</p></div>
    </div>
    <div class="service">
      <svg width="66" height="66" viewBox="0 0 66 66"><path d="M33 3a30 30 0 0 1 0 60" fill="none" stroke="#1fa9d6" stroke-width="3"/><path d="M33 63a30 30 0 0 1 0-60" fill="none" stroke="#b5e21c" stroke-width="3"/><circle cx="33" cy="33" r="14" fill="none" stroke="#fff" stroke-width="2"/><circle cx="33" cy="33" r="8" fill="none" stroke="#fff" stroke-width="2"/><circle cx="33" cy="33" r="2.5" fill="#fff"/></svg>
      <div><h3>Local Expertise</h3><p>Florida-based team that understands the needs of Orlando and statewide homeowners.</p></div>
    </div>
    <div class="service">
      <svg width="66" height="66" viewBox="0 0 66 66"><path d="M33 3a30 30 0 0 1 0 60" fill="none" stroke="#b5e21c" stroke-width="3"/><path d="M33 63a30 30 0 0 1 0-60" fill="none" stroke="#1fa9d6" stroke-width="3"/><path d="M33 40 V24 M33 30 C27 30 24 26 24 21 C29 21 33 24 33 30 M33 28 C38 28 42 24 42 19 C37 19 33 22 33 28" fill="none" stroke="#fff" stroke-width="2"/><path d="M20 42 H32 L42 38" fill="none" stroke="#fff" stroke-width="2"/></svg>
      <div><h3>Eco-Friendly</h3><p>Clean, renewable solar energy that helps reduce your carbon footprint.</p></div>
    </div>
  </section>

  <footer class="contact-band">
    <div class="address">
      <svg width="18" height="26" viewBox="0 0 18 26"><path d="M9 1a8 8 0 0 1 8 8c0 6-8 16-8 16S1 15 1 9a8 8 0 0 1 8-8z" fill="none" stroke="#25286a" stroke-width="2.2"/><circle cx="9" cy="9" r="3" fill="#25286a"/></svg>
      <div>Brightvale Energy, LLC<br>1420 Harbor Crest Road<br>Orlando, FL 32801</div>
    </div>
    <div class="phone">
      <svg width="18" height="28" viewBox="0 0 18 28"><path d="M12 2 L6 3 C2 8 2 20 6 25 L12 26 L13 20 L9 18 C8 15 8 13 9 10 L13 8 Z" fill="none" stroke="#25286a" stroke-width="2.4" stroke-linejoin="round"/></svg>
      555.010.2040
    </div>
    <div class="web">
      <div><svg width="11" height="8" viewBox="0 0 11 8"><rect x=".5" y=".5" width="10" height="7" fill="#25286a"/><path d="M.5 .5 L5.5 4.5 L10.5 .5" fill="none" stroke="#1fb1b3"/></svg>info@brightvaleenergy.com</div>
      <div><svg width="11" height="11" viewBox="0 0 11 11"><circle cx="5.5" cy="5.5" r="4.5" fill="none" stroke="#25286a" stroke-width="1.4"/><path d="M1 5.5 H10 M5.5 1 C3 4 3 7 5.5 10 C8 7 8 4 5.5 1" fill="none" stroke="#25286a"/></svg>www.brightvaleenergy.com</div>
    </div>
  </footer>
</main>
</body>
</html>
```